One Pager Website for various security awareness videos

We need a one pager website (design & coding) for our security awareness video series. We imagine placing a few (3-4 sample videos) on the website, a customer referal and some contact form. SOmething similar to https://quorvel.com/watch-now/. Here are some of the videos which we will place on the website:
https://www.streamdeck-example.net/watch?v=Hq7PzkA2mLd&t=112s
https://www.streamdeck-example.net/watch?v=Vb3RkeWn8Ts
https://www.streamdeck-example.net/watch?v=Jw9CdpLr4Ya
https://www.streamdeck-example.net/watch?v=Tz6GyqBn2Kx
https://www.streamdeck-example.net/watch?v=Rm4XhaPe7Qu
https://www.streamdeck-example.net/watch?v=Ed8WokSj3Lf
https://www.streamdeck-example.net/watch?v=Ny2BquTc5Hv
https://www.streamdeck-example.net/watch?v=Pk5FsmVd9Ga
https://www.streamdeck-example.net/watch?v=Wc7JteHn3Rb
As for logo: our company www.tembrashield.com is the creator of those videos. You can use our logo / name.
Target Market(s)
B2B security officers in large enterprises
Coding
Coded - Design and coding required
Number of Pages Required
1 page
Look and feel

```html
<!DOCTYPE html>
<html lang="en">
<head>
<meta charset="utf-8">
<title>Tembra — Security Awareness Video Series</title>
<link rel="stylesheet" href="https://fonts.googleapis.com/css2?family=Poppins:wght@400;500;600;700&display=swap">
<style>
  :root{
    --teal:#1bb2c0;
    --teal-dark:#0f8f9c;
    --teal-deep:#0b6f7a;
    --yellow:#f8b41c;
    --orange:#f39a1e;
    --ink:#2f3438;
    --muted:#7b8287;
    --line:#d9dee1;
    --paper:#ffffff;
    --soft:#f3f5f6;
  }
  *{box-sizing:border-box;margin:0;padding:0}
  html,body{width:1200px;height:3420px;overflow:hidden}
  body{font-family:"Poppins",sans-serif;color:var(--ink);background:var(--paper)}

  .hero{position:relative;height:440px;overflow:hidden}
  .hero-photo{position:absolute;inset:0;background:linear-gradient(120deg,#0e7d88 0%,#1bb2c0 45%,#5fcfd8 100%)}
  .hero-photo::after{content:"";position:absolute;inset:0;background:rgba(27,178,192,.35)}
  .brand{position:absolute;left:48px;top:30px;display:flex;align-items:center;gap:10px;z-index:2}
  .brand-dot{width:34px;height:34px;border-radius:50%;background:var(--yellow)}
  .brand-name{font-weight:700;font-size:30px;color:#fff}
  .hero-title{position:absolute;top:150px;width:100%;text-align:center;z-index:2;color:#fff;font-weight:700;font-size:58px;line-height:1.15}
  .hero-title .mark{position:relative;display:inline-block}
  .hero-title .mark::after{content:"";position:absolute;left:0;right:0;bottom:4px;height:8px;background:var(--yellow);border-radius:4px}
  .scroll-cue{position:absolute;left:50%;bottom:-2px;transform:translate(-50%,50%);width:64px;height:64px;border-radius:50%;background:var(--yellow);z-index:3;display:flex;align-items:center;justify-content:center}

  .latest{height:680px;text-align:center;padding-top:70px}
  .section-title{font-weight:700;font-size:36px;line-height:1.2;color:var(--ink)}
  .episode-tag{display:inline-block;margin-top:18px;background:var(--teal);color:#fff;font-weight:600;font-size:16px;letter-spacing:.5px;padding:9px 26px}
  .episode-name{margin-top:22px;font-size:26px;font-weight:500;letter-spacing:1px}
  .lede{width:720px;margin:14px auto 0;font-size:14px;line-height:1.7;color:var(--muted)}
  .feature-video{position:relative;width:460px;height:250px;margin:30px auto 0;border:3px solid var(--teal);box-shadow:0 8px 22px rgba(0,0,0,.12)}

  .thumb{position:absolute;inset:0;background:linear-gradient(180deg,#fbfbfb,#e4e7e9)}
  .play{position:absolute;left:50%;top:50%;transform:translate(-50%,-50%)}

  .release-band{height:50px;background:var(--yellow);color:#fff;font-weight:600;font-size:16px;letter-spacing:2px;display:flex;align-items:center;justify-content:center}

  .lineup{height:940px;padding:56px 150px 0}
  .lineup .section-title{text-align:left}
  .lineup .lede{width:auto;margin:12px 0 0;text-align:left}
  .video-grid{display:grid;grid-template-columns:1fr 1fr;column-gap:60px;row-gap:50px;margin-top:40px}
  .video-card{text-align:center}
  .video-frame{position:relative;height:250px;box-shadow:0 8px 22px rgba(0,0,0,.14)}
  .video-title{margin-top:16px;font-weight:600;font-size:17px}
  .video-note{margin-top:4px;font-size:13px;color:var(--muted)}

  .referral{height:540px;background:linear-gradient(135deg,var(--teal) 0%,var(--teal-dark) 100%);padding-top:52px;text-align:center}
  .referral .section-title{color:#fff;font-size:32px}
  .testimonial{position:relative;width:820px;height:320px;margin:36px auto 0;background:var(--paper);display:flex;align-items:center;gap:44px;padding:0 60px;text-align:left;box-shadow:0 12px 30px rgba(0,0,0,.18)}
  .testimonial-top{position:absolute;top:-16px;left:50%;transform:translateX(-50%);width:32px;height:32px;border-radius:50%;background:var(--paper);display:flex;align-items:center;justify-content:center}
  .avatar{flex:none;width:170px;height:170px;border-radius:50%;background:linear-gradient(160deg,#e9c9a8,#b4876a)}
  .quote-text{font-size:14px;line-height:1.8;color:var(--muted)}
  .quote-name{margin-top:16px;font-weight:600;font-size:20px;color:var(--orange)}
  .quote-mark{position:absolute;right:40px;bottom:-38px}

  .contact{height:620px;text-align:center;padding-top:70px}
  .contact .lede{width:560px}
  .contact-form{width:460px;margin:28px auto 0;display:flex;flex-direction:column;gap:14px}
  .field{height:40px;border:1px solid var(--line);font-family:inherit;font-size:13px;color:var(--muted);padding:0 14px;display:flex;align-items:center}
  .field-area{height:110px;align-items:flex-start;padding-top:10px}
  .submit{height:42px;background:var(--yellow);color:#fff;font-weight:600;font-size:15px;letter-spacing:1px;display:flex;align-items:center;justify-content:center;margin-top:6px}

  .site-footer{height:150px;background:var(--teal);position:relative;display:flex;align-items:center;padding:0 48px}
  .site-footer .brand{position:static}
  .footer-meta{margin-left:auto;text-align:right}
  .socials{display:flex;gap:10px;justify-content:flex-end}
  .socials span{width:30px;height:30px;border-radius:50%;background:#fff;opacity:.9}
  .copyright{margin-top:10px;font-size:12px;color:#e6f7f9}
</style>
</head>
<body>

<header class="hero">
  <div class="hero-photo" role="img" aria-label="Photo of a man working on a laptop in an office, tinted teal"></div>
  <div class="brand"><span class="brand-dot"></span><span class="brand-name">Tembra</span></div>
  <h1 class="hero-title">Our Security <span class="mark">Awareness</span><br>Video Series</h1>
  <div class="scroll-cue">
    <svg width="24" height="24" viewBox="0 0 24 24" fill="none" stroke="#fff" stroke-width="3" stroke-linecap="round" stroke-linejoin="round"><path d="M6 9l6 6 6-6"/></svg>
  </div>
</header>

<section class="latest">
  <h2 class="section-title">ONE OF OUR LATEST<br>EPISODES</h2>
  <div class="episode-tag">SEASON 4 | EPISODE 39</div>
  <p class="episode-name">DON'T FALL FOR IT</p>
  <p class="lede">Phishing emails look more convincing every year. In this episode our team shows how one rushed click can open the door to attackers, and what to check before you reply.</p>
  <div class="feature-video">
    <div class="thumb" role="img" aria-label="Episode illustration of a presenter beside a security awareness board"></div>
    <svg class="play" width="60" height="60" viewBox="0 0 60 60"><circle cx="30" cy="30" r="30" fill="var(--yellow)"/><path d="M24 18l18 12-18 12z" fill="#fff"/></svg>
  </div>
</section>

<div class="release-band">2021 - RELEASES</div>

<section class="lineup">
  <h2 class="section-title">OUR 2021 LINEUP:</h2>
  <p class="lede">Each month we release a short episode built on real attacks seen across large enterprises. Share them with your teams and turn everyday habits into your strongest line of defense.</p>
  <div class="video-grid">
    <article class="video-card">
      <div class="video-frame"><div class="thumb" role="img" aria-label="Episode illustration of an employee at a desk"></div>
        <svg class="play" width="54" height="54" viewBox="0 0 60 60"><circle cx="30" cy="30" r="30" fill="var(--yellow)"/><path d="M24 18l18 12-18 12z" fill="#fff"/></svg></div>
      <h3 class="video-title">Current Spoofs</h3>
      <p class="video-note">Spot fake senders before they reach your inbox.</p>
    </article>
    <article class="video-card">
      <div class="video-frame"><div class="thumb" role="img" aria-label="Episode illustration of an employee at a desk"></div>
        <svg class="play" width="54" height="54" viewBox="0 0 60 60"><circle cx="30" cy="30" r="30" fill="var(--yellow)"/><path d="M24 18l18 12-18 12z" fill="#fff"/></svg></div>
      <h3 class="video-title">Current Spoofs</h3>
      <p class="video-note">Learn the signs of a forged payment request.</p>
    </article>
    <article class="video-card">
      <div class="video-frame"><div class="thumb" role="img" aria-label="Episode illustration of an employee at a desk"></div>
        <svg class="play" width="54" height="54" viewBox="0 0 60 60"><circle cx="30" cy="30" r="30" fill="var(--yellow)"/><path d="M24 18l18 12-18 12z" fill="#fff"/></svg></div>
      <h3 class="video-title">Current Spoofs</h3>
      <p class="video-note">Why urgent calls from the boss deserve a pause.</p>
    </article>
    <article class="video-card">
      <div class="video-frame"><div class="thumb" role="img" aria-label="Episode illustration of an employee at a desk"></div>
        <svg class="play" width="54" height="54" viewBox="0 0 60 60"><circle cx="30" cy="30" r="30" fill="var(--yellow)"/><path d="M24 18l18 12-18 12z" fill="#fff"/></svg></div>
      <h3 class="video-title">Current Spoofs</h3>
      <p class="video-note">Check every link twice before you sign in.</p>
    </article>
  </div>
</section>

<section class="referral">
  <h2 class="section-title">CUSTOMER REFERAL</h2>
  <div class="testimonial">
    <div class="testimonial-top">
      <svg width="16" height="16" viewBox="0 0 24 24" fill="none" stroke="var(--teal)" stroke-width="3" stroke-linecap="round" stroke-linejoin="round"><path d="M6 15l6-6 6 6"/></svg>
    </div>
    <div class="avatar" role="img" aria-label="Portrait photo of the customer"></div>
    <div>
      <p class="quote-text">Our staff actually look forward to each new episode. The stories are short, clear and memorable, and our reported phishing attempts have doubled since we rolled out the series across all offices.</p>
      <p class="quote-name">Selina R.</p>
    </div>
    <svg class="quote-mark" width="70" height="60" viewBox="0 0 70 60"><path d="M0 60V34C0 16 8 5 26 0l3 8C19 12 15 19 15 28h13v32zM41 60V34C41 16 49 5 67 0l3 8C60 12 56 19 56 28h13v32z" fill="var(--yellow)"/></svg>
  </div>
</section>

<section class="contact">
  <h2 class="section-title">GET IN TOUCH</h2>
  <p class="lede">Have a question about the series? Send us a message and we will get back to you.</p>
  <form class="contact-form">
    <div class="field">Name</div>
    <div class="field">Email</div>
    <div class="field">Company</div>
    <div class="field field-area">Message</div>
    <div class="submit">Submit</div>
  </form>
</section>

<footer class="site-footer">
  <div class="brand"><span class="brand-dot"></span><span class="brand-name">Tembra</span></div>
  <div class="footer-meta">
    <div class="socials"><span></span><span></span><span></span></div>
    <p class="copyright">© 2021 Tembra. All rights reserved.</p>
  </div>
</footer>

</body>
</html>
```